Business Card with PUNCH
bluepinelodge.net
Project: Business Card with PUNCH
Business Card with PUNCH - Consulting
Creative Brief
Simple
Morris Trulsow
President
418 Dunmere Lane Suite 207 Spring, TX 77291
morris@bluepinelodge.net
logo on the back please
mtrulsow mtrulsow
WOW, what a tremendous effort overnight! Here is what I can tell you from what we have seen so far: 1. Prefer horizontal orientation of card rather than vertical. 2. Prefer the white cards with the blue and gray logo vs. the darker colors 3. Would like the back of the card to be white with room for a hand written note 4. Clear plastic cards are not a hit 5. Not a fan of card that look like the data is presented on any kind of a 'tab' or website type icons. Thanks for the many creative ideas, we are excited about this contest. mt

```html
<!DOCTYPE html>
<html lang="en">
<head>
<meta charset="utf-8">
<title>bluepinelodge – business card</title>
<link href="https://fonts.googleapis.com/css2?family=Roboto:wght@400;500;700&display=swap" rel="stylesheet">
<style>
  :root {
    --stage: #5b5b5b;
    --navy: #1a2580;
    --royal: #3347c4;
    --ink: #1e2f7a;
    --grey-text: #555a63;
    --light: #f4f4f6;
    --white: #ffffff;
    --silver: #b9bcc2;
    --accent: #3b8fd9;
  }
  * { margin: 0; padding: 0; box-sizing: border-box; }
  html, body { width: 1200px; height: 840px; overflow: hidden; }
  body {
    background: var(--stage);
    font-family: "Roboto", Arial, sans-serif;
    position: relative;
  }
  .card {
    position: absolute;
    width: 520px;
    height: 300px;
    top: 270px;
    overflow: hidden;
    box-shadow: 0 10px 24px rgba(0,0,0,.35);
  }
  .card-front { left: 60px; background: var(--light); }
  .card-back { left: 620px; background: var(--white); }
  .card svg.art { position: absolute; inset: 0; }

  .identity { position: absolute; right: 30px; top: 34px; text-align: right; }
  .identity .name { font-size: 20px; font-weight: 500; color: var(--ink); letter-spacing: 1px; }
  .identity .role { font-size: 12px; font-weight: 500; color: var(--ink); letter-spacing: 1px; margin-top: 3px; }

  .address {
    position: absolute; right: 30px; top: 112px; text-align: right;
    font-size: 11px; line-height: 16px; color: var(--grey-text); font-style: normal;
  }
  .contacts {
    position: absolute; right: 30px; top: 172px; list-style: none;
    font-size: 10px; color: var(--grey-text);
  }
  .contacts li {
    display: flex; justify-content: flex-end; align-items: center;
    gap: 6px; height: 19px;
  }
  .contacts svg { width: 10px; height: 10px; fill: var(--ink); flex: none; }

  .brand {
    position: absolute; font-weight: 700; letter-spacing: -0.5px;
    display: flex; align-items: center; gap: 6px; color: var(--ink);
  }
  .card-front .brand { left: 24px; bottom: 38px; font-size: 26px; }
  .card-back .brand { left: 26px; bottom: 44px; font-size: 30px; }
  .brand .dot { width: 12px; height: 12px; border-radius: 50%; background: var(--accent); }
</style>
</head>
<body>

<section class="card card-front">
  <svg class="art" viewBox="0 0 520 300" aria-hidden="true">
    <defs>
      <linearGradient id="blueField" x1="0" y1="0" x2="1" y2="1">
        <stop offset="0" stop-color="var(--navy)"/>
        <stop offset="1" stop-color="var(--royal)"/>
      </linearGradient>
      <linearGradient id="silverSwoosh" x1="0" y1="0" x2="1" y2="1">
        <stop offset="0" stop-color="#ffffff"/>
        <stop offset="0.5" stop-color="var(--silver)"/>
        <stop offset="1" stop-color="#8a8d94"/>
      </linearGradient>
    </defs>
    <path d="M0 0 H320 C250 30 220 90 170 135 C125 170 65 182 0 184 Z" fill="url(#blueField)"/>
    <path d="M320 0 H350 C280 40 250 110 195 152 C145 190 75 202 0 204 V184 C65 182 125 170 170 135 C220 90 250 30 320 0 Z" fill="url(#silverSwoosh)"/>
  </svg>

  <div class="identity">
    <p class="name">MORRIS TRULSOW</p>
    <p class="role">PRESIDENT</p>
  </div>

  <address class="address">
    418 Dunmere Lane Suite 207<br>Spring, TX 77291
  </address>

  <ul class="contacts">
    <li>014 555 0182 <svg viewBox="0 0 10 10"><path d="M2 0l2 2-1 1.5c.6 1.3 1.5 2.2 2.8 2.8L7.3 5 10 7 8.5 9.5C4 9.5.5 6 .5 1.5Z"/></svg></li>
    <li>014 555 0183 <svg viewBox="0 0 10 10"><rect x="2.5" y="0" width="5" height="10" rx="1"/></svg></li>
    <li>014 555 0184 <svg viewBox="0 0 10 10"><rect x="0" y="3" width="10" height="6" rx="1"/><rect x="2" y="0" width="6" height="3"/></svg></li>
    <li>morris@bluepinelodge.net <svg viewBox="0 0 10 10"><rect x="0" y="2" width="10" height="6.5" rx="1"/></svg></li>
    <li>www.bluepinelodge.net <svg viewBox="0 0 10 10"><circle cx="5" cy="5" r="5"/></svg></li>
  </ul>

  <div class="brand"><span class="dot"></span>bluepinelodge</div>
</section>

<section class="card card-back">
  <svg class="art" viewBox="0 0 520 300" aria-hidden="true">
    <defs>
      <linearGradient id="lightSwoosh" x1="0" y1="0" x2="1" y2="1">
        <stop offset="0" stop-color="#f2f3f5"/>
        <stop offset="0.45" stop-color="#b3b6bd"/>
        <stop offset="1" stop-color="#6f737b"/>
      </linearGradient>
    </defs>
    <path d="M520 0 V180 C470 150 420 80 380 0 Z" fill="#eef0f6"/>
    <path d="M360 0 H384 C420 80 468 150 520 176 V196 C462 166 404 92 360 0 Z" fill="url(#lightSwoosh)"/>
    <path d="M410 0 H430 C452 50 484 96 520 120 V134 C478 110 440 64 410 0 Z" fill="var(--royal)" opacity=".75"/>
  </svg>

  <div class="brand"><span class="dot"></span>bluepinelodge</div>
</section>

</body>
</html>
```